flatmoveria.co.uk landing page website design

Hi designers, I would like a custom designed landing page very similar to www.dwellotrade.co.uk. It represents a happy place, sunny days and people swapping homes. I would like this done just like theres but our own design but a similar layout as theres.

I would like the 3 reasons to use us to be

Connect to thousands of other people in your area looking for a home swap

Our service is Completely free unlike most other exchange websites.

Find a exchange within 30 days!*

Thank you all,

Hi Everyone, I need the designs to represent london if possible like one of the designers has done for anyone else being in with a chance to win. Please check out the design by RT with the london look. I still like some of the others and they may win but i need to give this a try please.

Council house tenants

• Custom designed landing page showing all the elements that www.dwellotrade.co.uk use, The blue sky, and the land it shows with houses and people representing people swapping house. It can not be the same as them but can be similar concept with our own custom design and colour scheme ect.

please create 3 bubbles for speech from people. Please add the following quotes. "Its time we upsize"
"lets try and downsize and save money" "shall we move house?"
Would like 2 blocks of flats in a similar way dwello trade.co.uk show the houses.

• Same colour scheme as dwello trade apart from the blue sky

```html
<!DOCTYPE html>
<html lang="en">
<head>
<meta charset="utf-8">
<title>flatmoveria.co.uk – Home Swap</title>
<link href="https://fonts.googleapis.com/css2?family=Poppins:wght@300;400;500;600;700&display=swap" rel="stylesheet">
<style>
:root{
  --green:#3cb94c;
  --green-light:#4cc45b;
  --black:#0b0b0b;
  --ink:#1b1b1b;
  --text:#444;
  --grey-bg:#f1f1f1;
  --sky-top:#9fd8f3;
  --sky-bottom:#e6f5fc;
  --white:#fff;
}
*{box-sizing:border-box;margin:0;padding:0}
html,body{width:1200px;height:3096px;overflow:hidden}
body{position:relative;font-family:'Poppins',sans-serif;color:var(--ink);background:var(--white)}
.abs{position:absolute}

/* Hero */
.hero{position:absolute;left:0;top:0;width:1200px;height:760px;background:linear-gradient(180deg,var(--sky-top) 0%,#c4e8f8 45%,var(--sky-bottom) 70%)}
.brand{left:162px;top:44px;display:flex;align-items:center;gap:10px;font-size:27px;font-weight:600;color:var(--ink)}
.brand-mark{width:30px;height:30px;border-radius:6px;background:var(--green)}
.btn{display:flex;align-items:center;justify-content:center;font-size:15px;font-weight:500;color:var(--white);border-radius:3px}
.btn-login{left:850px;top:46px;width:90px;height:31px;background:var(--green)}
.btn-register{left:950px;top:46px;width:90px;height:31px;background:var(--black)}
.hero-kicker{left:0;width:1200px;top:148px;text-align:center;font-size:24px;font-weight:400}
.hero-title{left:0;width:1200px;top:184px;text-align:center;font-size:36px;font-weight:600}
.hero-title span{color:var(--green)}
.hero-note{left:0;width:1200px;top:241px;text-align:center;font-size:20px;font-weight:600;color:var(--green)}
.search{left:160px;top:298px;width:880px;height:87px;background:var(--green);border-radius:2px}
.field-label{position:absolute;top:14px;font-size:15px;color:var(--white);font-weight:500}
.field{position:absolute;top:35px;height:35px;background:var(--white);border-radius:2px;font-size:15px;color:#8a8a8a;padding:0 13px;display:flex;align-items:center;justify-content:space-between}
.btn-search{position:absolute;left:730px;top:34px;width:123px;height:35px;background:var(--black);color:var(--white);font-size:17px;font-weight:500;display:flex;align-items:center;justify-content:center;gap:10px;border-radius:2px}
.landscape{left:0;top:380px;width:1200px;height:380px}
.bubble{position:absolute;background:var(--white);border-radius:8px;font-size:13px;line-height:19px;text-align:center;display:flex;align-items:center;justify-content:center;box-shadow:0 2px 6px rgba(0,0,0,.08)}
.bubble::after{content:"";position:absolute;bottom:-12px;left:55%;border:8px solid transparent;border-top:12px solid var(--white);border-bottom:0}

/* Audience toggle */
.audience{left:323px;top:838px;width:553px;height:52px;border-radius:26px;overflow:hidden;display:flex;font-size:15.5px;color:var(--white)}
.audience div{flex:1;display:flex;align-items:center;justify-content:center;font-weight:500}
.audience .tenant{background:var(--green)}
.audience .landlord{background:var(--black)}
.audience span{font-weight:300}

/* About */
.about-art{left:160px;top:930px;width:320px;height:260px;border-radius:4px;background:linear-gradient(135deg,#e9f6eb 0%,#f4f4f4 100%)}
.about-kicker{left:559px;top:990px;font-size:19px;font-weight:400;color:var(--ink)}
.about-title{left:559px;top:1022px;font-size:38px;font-weight:700;letter-spacing:.3px}
.about-text{left:559px;top:1082px;width:480px;font-size:14.5px;line-height:22.5px;color:var(--text)}
.about-text p+p{margin-top:7px}
.btn-learn{left:560px;top:1223px;width:133px;height:41px;background:var(--green);font-size:16px}

/* Stats */
.stats-band{left:0;top:1370px;width:1200px;height:1000px;background:var(--grey-bg)}
.card{position:absolute;top:1467px;width:248px;height:268px;background:var(--white);clip-path:polygon(0 30px,50% 0,100% 30px,100% 100%,0 100%);text-align:center;filter:drop-shadow(0 4px 6px rgba(0,0,0,.08))}
.card.is-green{background:var(--green-light);color:var(--white)}
.card-num{position:absolute;top:40px;left:0;width:100%;font-size:31px;font-weight:500}
.card-sub{position:absolute;left:0;width:100%;font-size:19px;font-weight:500}
.card-text{position:absolute;left:0;width:100%;font-size:18px;line-height:24px}
.bar{position:absolute;left:27px;top:100px;width:194px;height:5px;background:rgba(255,255,255,.35);border-radius:3px}
.bar i{display:block;width:92%;height:100%;background:var(--white);border-radius:3px}
.card svg{position:absolute;left:50%;transform:translateX(-50%)}

/* Contact */
.contact{left:188px;top:1865px;width:826px;height:338px;background:var(--white);box-shadow:0 2px 10px rgba(0,0,0,.05)}
.contact-side{position:absolute;left:0;top:0;width:392px;height:338px;background:linear-gradient(170deg,var(--green-light) 60%,var(--green) 60%);color:var(--white);text-align:center}
.contact-title{position:absolute;top:80px;width:100%;font-size:25px;font-weight:600}
.contact-lead{position:absolute;top:126px;width:100%;font-size:13px;line-height:22px;font-weight:600}
.input{position:absolute;left:450px;width:315px;border:1px solid #cfcfcf;border-radius:2px;font-size:14px;color:#888;padding:0 14px;display:flex;align-items:center}
.btn-send{position:absolute;left:627px;top:264px;width:138px;height:35px;background:var(--green);color:var(--white);font-size:15px;display:flex;align-items:center;justify-content:center;border-radius:2px}

/* CTA */
.cta{left:0;top:2340px;width:1200px;height:460px}
.cta-title{left:0;width:1200px;top:2440px;text-align:center;font-size:36px;font-weight:300;color:var(--white)}
.cta-title b{font-weight:600}
.cta-text{left:0;width:1200px;top:2494px;text-align:center;font-size:16px;line-height:24px;color:var(--white)}
.btn-call{left:516px;top:2574px;width:168px;height:42px;background:var(--black);border-radius:21px;font-size:17px}

/* Footer */
.footer{left:0;top:2750px;width:1200px;height:346px;background:var(--black)}
.foot-head{position:absolute;font-size:14px;font-weight:600;color:var(--white)}
.foot-links{position:absolute;list-style:none;font-size:12.5px;color:#cfcfcf;line-height:25.7px}
.foot-item{position:absolute;left:162px;display:flex;gap:10px;font-size:12.5px;line-height:20px;color:#dcdcdc}
.foot-item svg{flex:none;margin-top:2px}
.news-text{position:absolute;left:749px;top:122px;width:170px;font-size:10.5px;line-height:21px;color:#cfcfcf}
.news{position:absolute;left:738px;top:180px;width:270px;height:35px;border-radius:18px;overflow:hidden;display:flex}
.news-input{flex:1;background:var(--white);font-size:12.5px;color:#777;display:flex;align-items:center;padding-left:22px}
.news-btn{width:108px;background:var(--green);color:var(--white);font-size:13.5px;font-weight:600;display:flex;align-items:center;justify-content:center}
.foot-rule{position:absolute;left:0;top:276px;width:1200px;height:1px;background:#222}
.copyright{position:absolute;left:121px;top:306px;font-size:12.5px;color:#cfcfcf}
.social{position:absolute;left:874px;top:296px;width:124px;height:30px;background:#2a2a2a;display:flex;align-items:center;justify-content:center;gap:12px}
.social i{width:9px;height:9px;border-radius:50%;background:#bdbdbd;display:block}
</style>
</head>
<body>

<section class="hero">
  <svg class="abs landscape" viewBox="0 0 1200 380" role="img" aria-label="Illustrated sunny countryside with green hills, trees, houses, two blocks of flats and families talking about swapping homes">
    <defs>
      <linearGradient id="hillFill" x1="0" y1="0" x2="0" y2="1">
        <stop offset="0" stop-color="#8fd06a"/>
        <stop offset="1" stop-color="#3f9a3a"/>
      </linearGradient>
    </defs>
    <path d="M0 150 C150 60 300 120 430 110 C560 100 700 40 860 90 C980 120 1100 70 1200 100 L1200 370 C1000 360 800 350 600 350 C400 350 200 345 0 352 Z" fill="url(#hillFill)"/>
  </svg>

  <div class="abs brand"><span class="brand-mark"></span>flatmoveria.co.uk</div>
  <div class="abs btn btn-login">Login</div>
  <div class="abs btn btn-register">Register</div>

  <p class="abs hero-kicker">Connect To Thousands Of Other People In Your Area</p>
  <h1 class="abs hero-title">Looking For A <span>Home</span> Swap</h1>
  <p class="abs hero-note">Find a exchange within 30 days!*</p>

  <form class="abs search">
    <span class="field-label" style="left:26px">Location</span>
    <div class="field" style="left:24px;width:219px">Town or Postcode</div>
    <span class="field-label" style="left:262px">Bedrooms</span>
    <div class="field" style="left:259px;width:219px">Any
      <svg width="14" height="8" viewBox="0 0 14 8"><path d="M1 1l6 6 6-6" fill="none" stroke="#888" stroke-width="1.3"/></svg></div>
    <span class="field-label" style="left:497px">Max. Rent ( £ Per Month )</span>
    <div class="field" style="left:494px;width:219px">Any
      <svg width="14" height="8" viewBox="0 0 14 8"><path d="M1 1l6 6 6-6" fill="none" stroke="#888" stroke-width="1.3"/></svg></div>
    <div class="btn-search">Search
      <svg width="18" height="18" viewBox="0 0 18 18"><circle cx="7.5" cy="7.5" r="6" fill="none" stroke="#fff" stroke-width="1.6"/><path d="M12 12l5 5" stroke="#fff" stroke-width="1.6"/></svg></div>
  </form>

  <div class="bubble" style="left:117px;top:414px;width:121px;height:73px">Its time<br>we upsize</div>
  <div class="bubble" style="left:438px;top:414px;width:152px;height:73px">Lets try and<br>downsize and<br>save money</div>
  <div class="bubble" style="left:872px;top:479px;width:120px;height:72px">Shall we<br>move house?</div>
</section>

<div class="abs audience">
  <div class="tenant">Are you a tenant?&nbsp;<span>Click here</span></div>
  <div class="landlord">Are you a landlord?&nbsp;<span>Click here</span></div>
</div>

<section>
  <div class="abs about-art" role="img" aria-label="Decorative emblem of two houses exchanging places with scattered dots"></div>
  <p class="abs about-kicker">About Company</p>
  <h2 class="abs about-title">WHY CHOOSE US</h2>
  <div class="abs about-text">
    <p>Our service is Completely free unlike most other exchange websites. We are changing the way people exchange council homes</p>
    <p>It can be a difficult and time consuming process finding your next property exchange. Our free service is proven to find your home swap faster with very little stress</p>
  </div>
  <div class="abs btn btn-learn">Learn More</div>
</section>

<div class="abs stats-band"></div>

<section>
  <div class="card" style="left:196px">
    <div class="card-num">200,000</div>
    <div class="card-sub" style="top:85px">Live Adverts</div>
    <svg style="top:120px" width="40" height="56" viewBox="0 0 40 56" fill="none" stroke="#111" stroke-width="1.6">
      <rect x="6" y="2" width="28" height="52" rx="3"/><path d="M12 20h10l6-5v16l-6-5H12z"/><text x="20" y="46" font-size="10" font-family="Poppins,sans-serif" text-anchor="middle" fill="#111" stroke="none">LIVE</text>
    </svg>
    <div class="card-text" style="top:202px">More than any other<br>swapping site!</div>
  </div>

  <div class="card is-green" style="left:476px">
    <div class="card-num">90%</div>
    <div class="bar"><i></i></div>
    <svg style="top:118px" width="56" height="56" viewBox="0 0 56 56" fill="none" stroke="#fff" stroke-width="1.6">
      <path d="M14 26a16 16 0 0 1 28-10"/><path d="M38 10l4 6-7 1"/><path d="M42 30a16 16 0 0 1-28 10"/><path d="M18 46l-4-6 7-1"/>
    </svg>
    <div class="card-text" style="top:188px">Get mathes<br>within 24 hours</div>
  </div>

  <div class="card" style="left:756px">
    <div class="card-num">23.2m</div>
    <svg style="top:110px" width="54" height="54" viewBox="0 0 54 54" fill="none" stroke="#111" stroke-width="2">
      <rect x="2" y="2" width="20" height="20" rx="2"/><rect x="32" y="2" width="20" height="20" rx="2"/><rect x="2" y="32" width="20" height="20" rx="2"/><rect x="32" y="32" width="20" height="20" rx="2"/>
    </svg>
    <div class="card-text" style="top:188px">Pageviews<br>per month</div>
  </div>
</section>

<section class="abs contact">
  <div class="contact-side">
    <h3 class="contact-title">Contact Form</h3>
    <p class="contact-lead">We are always happy to hear from you Call us<br>today to see how we can help you.</p>
    <svg class="abs" style="left:138px;top:226px" width="80" height="66" viewBox="0 0 80 66" fill="none" stroke="#fff" stroke-width="1.8">
      <ellipse cx="30" cy="24" rx="27" ry="20"/><path d="M12 40l-4 14 14-9"/><ellipse cx="52" cy="40" rx="22" ry="16" fill="#3cb94c"/><path d="M66 52l6 10-12-6"/>
    </svg>
    <div class="abs" style="left:262px;top:236px;width:40px;height:40px;border-radius:4px;background:#fff;opacity:.9"></div>
  </div>
  <div class="input" style="top:72px;height:35px">Name</div>
  <div class="input" style="top:124px;height:35px">Email</div>
  <div class="input" style="top:175px;height:68px;align-items:flex-start;padding-top:12px">Message</div>
  <div class="btn-send">Send Message</div>
</section>

<svg class="abs cta" viewBox="0 0 1200 460" preserveAspectRatio="none" aria-hidden="true">
  <path d="M0 35 C100 20 200 38 300 28 C420 18 520 36 640 26 C760 16 880 36 1000 26 C1100 18 1160 30 1200 26 L1200 460 L0 460 Z" fill="var(--green)"/>
  <path d="M0 415 C150 395 300 420 450 400 C600 380 700 405 850 395 C1000 385 1100 400 1200 395 L1200 460 L0 460 Z" fill="var(--black)"/>
</svg>
<h2 class="abs cta-title"><b>Call us</b> or leave us your details.</h2>
<p class="abs cta-text">We need to know some details about your property and your requirements for<br>the next one your looking for so we can move on to step</p>
<div class="abs btn btn-call">Call Now</div>

<footer class="abs footer">
  <h4 class="foot-head" style="left:162px;top:88px">Contact Us</h4>
  <div class="foot-item" style="top:126px">
    <svg width="14" height="16" viewBox="0 0 14 16" fill="none" stroke="#ddd" stroke-width="1.3"><path d="M7 15s5-5 5-9A5 5 0 0 0 2 6c0 4 5 9 5 9z"/><circle cx="7" cy="6" r="2"/></svg>
    <span>27 Larkmoor Lane<br>Brindle Vale BV4 2QT</span>
  </div>
  <div class="foot-item" style="top:178px">
    <svg width="16" height="16" viewBox="0 0 16 16" fill="#ddd"><path d="M3 1l3 3-2 2c1 2 3 4 5 5l2-2 3 3-2 3C6 15 1 10 1 3z"/></svg>
    <span>(020) 7946 0318</span>
  </div>
  <div class="foot-item" style="top:215px">
    <svg width="15" height="12" viewBox="0 0 15 12" fill="none" stroke="#ddd" stroke-width="1.2"><rect x="1" y="1" width="13" height="10"/><path d="M1 1l6.5 6L14 1"/></svg>
    <span>hello@flatmoveria.co.uk</span>
  </div>

  <h4 class="foot-head" style="left:421px;top:88px">Quick Links</h4>
  <ul class="foot-links" style="left:421px;top:114px"><li>Home</li><li>About Us</li><li>Why Us</li><li>Our Services</li><li>Blog</li></ul>

  <h4 class="foot-head" style="left:565px;top:88px">Quick Links</h4>
  <ul class="foot-links" style="left:565px;top:114px"><li>Support</li><li>Testimonials</li><li>Sitemap</li><li>Career</li><li>Contact Us</li></ul>

  <h4 class="foot-head" style="left:749px;top:88px">WRITE TO US</h4>
  <p class="news-text">Provide your email below to subscribe to our newsletter</p>
  <div class="news"><div class="news-input">Email address</div><div class="news-btn">Subscribe</div></div>

  <div class="foot-rule"></div>
  <p class="copyright">Copyright 2020 flatmoveria</p>
  <div class="social" aria-label="Social links"><i></i><i></i><i></i><i></i><i></i></div>
</footer>

</body>
</html>
```